New Landing page and designwork for Brindlequay.com

I need a brand new website landing page for Brindlequay.com + graphic work on that page as well. Including perhaps a logo design as well For Brindlequay

There is a new fill out form that needs to be integrated that I can provide to be part of the design, there are several different forms, which I have copied down in the Must Have section, only one of the forms need to be utilised. It is up to you to select the best form for your design.

This is a simple page that needs the form to be integrated, with nice graphic work and layout as well. There will be some changes to the wording of the bullet text points that are on the current website. This is a personal cash loan site, which will expand out to all various loan offerings, so please keep in mind some expandability for this.

Green color and Money Signs, Cash, etc are all nice elements to be used in the design as well.

Other items such as frequently asked questions, can be used from the current site

Target Market(s)

People looking for Personal Loans, Payday Loans, and eventually all other various forms of loans on other pages.

Industry/Entity Type

Loan

Requirements
Must have
• One of these forms must be utilised in the design - I like all three forms, but 1st form is nice since it is all on one page, The form codes are attached as a text file uploaded onto this brief. let me know of any issues please.
Should not have
• Do not use the Text "No Credit Check" or the text "Instantly Approved"

```html
<!DOCTYPE html>
<html lang="en">
<head>
<meta charset="UTF-8">
<title>Brindlequay.com – Cash Loans</title>
<link href="https://fonts.googleapis.com/css2?family=Archivo+Narrow:wght@400;700&family=Roboto+Condensed:wght@400;700&family=Noto+Sans:wght@400;700&display=swap" rel="stylesheet">
<style>
  :root {
    --ink: #000000;
    --green: #00ff00;
    --green-soft: #b8ffb0;
    --form-bg: #d3e9fb;
    --form-top: #b9dcf7;
    --form-title: #0d4f9c;
    --link-blue: #1a55b0;
    --field-border: #7fa6cf;
    --flag-red: #e0201c;
    --cash-green: #a9b79a;
    --cash-light: #e3e6d9;
    --kite: #2aa3e6;
    --mosaiq: #c8161e;
    --tribely: #2f4f93;
    --ledgerly: #1f7fbd;
  }
  * { box-sizing: border-box; margin: 0; padding: 0; }
  html, body { width: 1200px; height: 675px; overflow: hidden; background: #fff; }
  body { position: relative; font-family: "Archivo Narrow", "Arial Narrow", sans-serif; color: var(--ink); }

  .brand { position: absolute; left: 68px; top: 44px; font-weight: 700; font-size: 62px; letter-spacing: -2px; line-height: 1; white-space: nowrap; }
  .contact { position: absolute; right: 51px; top: 64px; font-size: 20px; letter-spacing: -0.4px; white-space: nowrap; }
  .main-nav { position: absolute; right: 51px; top: 121px; display: flex; gap: 22px; font-size: 20px; letter-spacing: -0.4px; white-space: nowrap; }
  .main-nav a { color: var(--ink); text-decoration: none; }
  .rule { position: absolute; left: 16px; top: 161px; width: 1164px; height: 11px; background: var(--green); }

  .welcome { position: absolute; left: 75px; top: 192px; font-size: 41px; font-weight: 700; letter-spacing: -1px; white-space: nowrap; }
  .intro { position: absolute; left: 38px; top: 244px; width: 640px; font-size: 18px; line-height: 27px; letter-spacing: -0.3px; text-indent: 12px; }
  .cash-photo { position: absolute; left: 94px; top: 388px; width: 187px; height: 250px;
    background: linear-gradient(160deg, var(--cash-light), var(--cash-green) 60%, #e9c7b0); border-radius: 40% 40% 20% 20%; }
  .approval { position: absolute; left: 295px; top: 392px; width: 385px; font-size: 18px; line-height: 27px; letter-spacing: -0.3px; }

  .loan-form { position: absolute; left: 711px; top: 186px; width: 421px; height: 316px; border-radius: 20px;
    background: linear-gradient(180deg, var(--form-top), var(--form-bg) 55%); font-family: "Noto Sans", Verdana, sans-serif; }
  .form-title { position: absolute; left: 26px; top: 4px; font-family: "Roboto Condensed", sans-serif; font-size: 25px; color: var(--form-title); white-space: nowrap; letter-spacing: -0.3px; }
  .form-title b { font-weight: 700; }
  .form-title span { color: #111; }
  .row { position: absolute; left: 26px; width: 368px; display: flex; justify-content: space-between; align-items: center; font-size: 11px; font-weight: 700; }
  .field { width: 173px; height: 20px; border: 1px solid var(--field-border); background: #fff; font-size: 11px; font-weight: 400; padding: 2px 4px; display: flex; justify-content: space-between; align-items: center; }
  .field .caret { width: 14px; height: 14px; border: 1px solid #999; background: #eee; font-size: 8px; text-align: center; line-height: 12px; }
  .agree { position: absolute; left: 30px; top: 172px; width: 370px; font-size: 11px; font-weight: 700; line-height: 14px; display: flex; gap: 8px; }
  .box { flex: none; width: 13px; height: 13px; border: 1px solid #777; background: #fff; }
  .agree a { color: var(--link-blue); }
  .canada { position: absolute; left: 26px; top: 236px; display: flex; gap: 8px; align-items: center; font-size: 11px; font-weight: 700; }
  .flag { width: 33px; height: 20px; background: linear-gradient(90deg, var(--flag-red) 25%, #fff 25%, #fff 75%, var(--flag-red) 75%); }
  .next { position: absolute; left: 302px; top: 229px; width: 90px; height: 34px; border-radius: 17px; border: 2px solid #9cc6e6;
    background: linear-gradient(#f5fbff, #cfe6f7); color: #2a73b5; font-size: 18px; font-weight: 700; display: flex; align-items: center; justify-content: center; gap: 4px; }

  .social { position: absolute; left: 923px; top: 568px; display: flex; gap: 15px; }
  .social span { width: 46px; height: 46px; border-radius: 9px; color: #fff; font-family: "Noto Sans", sans-serif; font-size: 8px; font-weight: 700; display: flex; align-items: flex-end; justify-content: center; padding-bottom: 4px; }
  .kite { background: var(--kite); } .mosaiq { background: var(--mosaiq); } .tribely { background: var(--tribely); } .ledgerly { background: var(--ledgerly); }

  .footer { position: absolute; left: 16px; top: 608px; width: 1164px; height: 56px; background: linear-gradient(180deg, #fff, var(--green-soft) 40%, var(--green)); text-align: center; font-size: 19px; letter-spacing: -0.4px; padding-top: 3px; line-height: 27px; padding-left: 12px; }
</style>
</head>
<body>
  <div class="brand">Brindlequay.com</div>
  <div class="contact">Contact Us 1.800.555.0142</div>
  <nav class="main-nav">
    <a>Home</a><a>About Us</a><a>Apply For A Loan</a><a>Loan Modification</a><a>Auto Loans</a><a>Free Credit Report</a><a>FAQ</a>
  </nav>
  <div class="rule"></div>

  <h1 class="welcome">Welcome to Brindlequay.com</h1>
  <p class="intro">Brindlequay.com is the quickest way to obtain secure, online cash advance and payday loans. Applying and qualifying for a payday loan is quick and very easy. Once you're approved for the cash advance, we'll electronically deposit the payday loan amount directly into your checking or savings account. We offer flexible payment options and discreet service that gets you the cash you need right now for your immediate cash needs. This is the best and easiest way for payday loans.</p>
  <div class="cash-photo" role="img" aria-label="Hand holding a fan of hundred-dollar bills"></div>
  <p class="approval">The approval process is very quick and easy and you will have your cash within minutes upon completion of the easy form to the top right of this page. Guaranteed Results.</p>

  <form class="loan-form">
    <div class="form-title"><b>Get Cash Now!</b> <span>Up to $1000 Cash Loan</span></div>
    <div class="row" style="top:56px">Select Your Loan Amount:<div class="field">$500<span class="caret">▼</span></div></div>
    <div class="row" style="top:98px">E-Mail Address:<div class="field"></div></div>
    <div class="row" style="top:140px">State:<div class="field">Select One<span class="caret">▼</span></div></div>
    <div class="agree"><span class="box"></span><span>I certify that I have read &amp; agree to the <a>Privacy Policy</a> &amp; <a>Terms of Use</a></span></div>
    <div class="canada"><span class="flag" role="img" aria-label="Canadian flag"></span>Canadian Residents - Click Here!</div>
    <div class="next">Next <svg width="10" height="12" viewBox="0 0 10 12"><path d="M2 1 L8 6 L2 11" fill="none" stroke="#2a73b5" stroke-width="3"/></svg></div>
  </form>

  <div class="footer">Privacy Policy | Frequently Asked Questions &nbsp;| Terms and Conditions | Sitemap<br>Copyright Brindlequay.com</div>
  <div class="social">
    <span class="kite">Kitewire</span><span class="mosaiq">Mosaiq</span><span class="tribely">Tribely</span><span class="ledgerly">Ledgerly</span>
  </div>
</body>
</html>
```